Business Card design for new private practice opening

I need a business card design for my new private practice with my new logo uploaded as a file
On the front the logo
On the back: maybe a small logo somewhere?
Priv. Doz. DDr. Corinna Vestaluk
Fachärztin für Allgemein- & Viszeralchirurgie
Address: xxx
Tel: xxx
Mobil:xxx
Webseite:xxx
Email:xxx

Contact Information for Business Card

See project description above for details

Requirements
Nice to have
• I would like the colors of the logo incorporated into the business card

```html
<!DOCTYPE html>
<html lang="de">
<head>
<meta charset="utf-8">
<title>Vestaluk Chirurgie – Visitenkarte</title>
<link href="https://fonts.googleapis.com/css2?family=Montserrat:wght@400;500;600;700&display=swap" rel="stylesheet">
<style>
  :root{
    --page:#e6e6e6;
    --teal:#45b8b4;
    --teal-dark:#3aa9a5;
    --teal-light:#4fc3bf;
    --card-light:#f4f4f4;
    --mark-faint:#e4e4e4;
    --text-grey:#6b6b6b;
    --rule:#9a9a9a;
    --white:#ffffff;
  }
  *{margin:0;padding:0;box-sizing:border-box}
  html,body{width:1200px;height:1000px;overflow:hidden}
  body{background:var(--page);font-family:"Montserrat",sans-serif;position:relative}
  .card{position:absolute;left:300px;width:600px;height:364px;border-radius:32px;overflow:hidden}
  .card-front{top:108px;background:var(--teal)}
  .card-back{top:526px;background:var(--card-light)}
  .front-pattern{position:absolute;inset:0;background:linear-gradient(100deg,var(--teal-dark) 0%,var(--teal) 50%,var(--teal-light) 100%)}
  .brand{position:absolute;display:flex;align-items:center;gap:8px}
  .brand-dot{width:44px;height:44px;border-radius:50%;flex:none}
  .brand-name{font-weight:600;line-height:1.12;letter-spacing:.2px}
  .card-front .brand{left:404px;top:256px}
  .card-front .brand-dot{border:3px solid var(--white)}
  .card-front .brand-name{color:var(--white);font-size:17px}
  .card-back .brand{left:38px;top:60px}
  .card-back .brand-dot{width:40px;height:40px;border:2px solid var(--teal)}
  .card-back .brand-name{color:var(--text-grey);font-size:16px;font-weight:500}
  .back-mark{position:absolute;left:272px;top:0;width:328px;height:364px;
    background:radial-gradient(circle at 70% 50%,var(--mark-faint) 0%,var(--mark-faint) 55%,rgba(228,228,228,0) 72%)}
  .person{position:absolute;left:37px;top:150px}
  .person-title,.person-name{color:var(--teal);font-weight:700;font-size:18px;line-height:25px}
  .person-role{color:var(--text-grey);font-size:14px;line-height:18px;margin-top:2px;padding-left:1px}
  .divider{position:absolute;left:38px;top:258px;width:532px;height:1px;background:var(--rule)}
  .contacts{position:absolute;left:46px;top:268px;list-style:none}
  .contacts li,.links li{display:flex;align-items:center;height:21.5px;color:var(--text-grey);font-size:14px}
  .contacts svg{width:12px;height:12px;margin-right:7px;fill:var(--teal)}
  .contacts .icon-box{width:19px;display:flex}
  .links{position:absolute;left:456px;top:289px;list-style:none}
  .links svg{width:12px;height:12px;margin-right:3px;fill:var(--teal)}
</style>
</head>
<body>

<section class="card card-front">
  <div class="front-pattern" role="img" aria-label="Embossed repeating pattern of the practice mark in tonal teal"></div>
  <div class="brand">
    <span class="brand-dot"></span>
    <span class="brand-name">VESTALUK<br>CHIRURGIE</span>
  </div>
</section>

<section class="card card-back">
  <div class="back-mark" role="img" aria-label="Large faint practice mark as background decoration"></div>
  <div class="brand">
    <span class="brand-dot"></span>
    <span class="brand-name">VESTALUK<br>CHIRURGIE</span>
  </div>
  <div class="person">
    <p class="person-title">Priv. Doz. DDr.</p>
    <p class="person-name">CORINNA VESTALUK</p>
    <p class="person-role">Fachärztin für Allgemein-<br>&amp; Viszeralchirurgie</p>
  </div>
  <div class="divider"></div>
  <ul class="contacts">
    <li><span class="icon-box"><svg viewBox="0 0 24 24"><path d="M6.6 10.8a15 15 0 0 0 6.6 6.6l2.2-2.2c.3-.3.7-.4 1-.2 1.1.4 2.3.6 3.6.6.6 0 1 .4 1 1V20c0 .6-.4 1-1 1A17 17 0 0 1 3 4c0-.6.4-1 1-1h3.5c.6 0 1 .4 1 1 0 1.3.2 2.5.6 3.6.1.3 0 .7-.2 1z"/></svg></span>Tel: xxx</li>
    <li><span class="icon-box"><svg viewBox="0 0 24 24"><rect x="6" y="1" width="12" height="22" rx="2"/></svg></span>Mobil:xxx</li>
    <li><span class="icon-box"><svg viewBox="0 0 24 24"><path d="M1 5h22v14H1z" fill="none"/><path d="M1 5h22v14H1zM2.5 6.5 12 13l9.5-6.5" fill="var(--teal)" stroke="var(--card-light)" stroke-width="1.3"/></svg></span>Email:xxx</li>
  </ul>
  <ul class="links">
    <li><svg viewBox="0 0 24 24"><path d="M12 2a10 10 0 1 0 0 20 10 10 0 0 0 0-20zm0 2c.8 1 1.6 2.7 1.9 5h-3.8c.3-2.3 1.1-4 1.9-5zM4.3 9a8 8 0 0 1 4.3-4.2C8 6 7.6 7.4 7.4 9zm0 6h3.1c.2 1.6.6 3 1.2 4.2A8 8 0 0 1 4.3 15zm5.8 0h3.8c-.3 2.3-1.1 4-1.9 5-.8-1-1.6-2.7-1.9-5zm0-2a18 18 0 0 1 0-2h3.8a18 18 0 0 1 0 2zm5.3 6.2c.6-1.2 1-2.6 1.2-4.2h3.1a8 8 0 0 1-4.3 4.2zM16.6 9c-.2-1.6-.6-3-1.2-4.2A8 8 0 0 1 19.7 9z"/></svg>Webseite</li>
    <li><svg viewBox="0 0 24 24"><path d="M12 1a8 8 0 0 0-8 8c0 6 8 14 8 14s8-8 8-14a8 8 0 0 0-8-8zm0 11a3 3 0 1 1 0-6 3 3 0 0 1 0 6z"/></svg>Austria</li>
  </ul>
</section>

</body>
</html>
```